Business acrd and Stationery desgin FOR DUNMORE

I want creative and expressive stationary design .on the front side for business card I need the logo and doctors name to be there and on the back side I need time and appointment .Please see attached business card to use same names ,but use address below and phone number

Note:the deigner must submit the file in vector format and PSD and PDF

Business name is :Dunmore Glen Medical Clinic.

Address:
20418 57 ST NW
City :EDMONTON AB
Postal code: T6K 3R8

Phone :(780) 555-0142
Fax:(780) 555-0187

Other Business name :Dunmore Medical Clinic

• logo in the back on business card

```html
<!DOCTYPE html>
<html lang="en">
<head>
<meta charset="utf-8">
<title>Dunmore Glen Medical Clinic – Stationery</title>
<link href="https://fonts.googleapis.com/css2?family=Open+Sans:wght@400;600;700&display=swap" rel="stylesheet">
<style>
:root{
  --blue:#1f3f8c;
  --red:#e3202a;
  --ink:#222;
  --grey:#666;
  --paper:#fff;
  --stage:#878787;
  --line:#9aa6c4;
}
*{box-sizing:border-box;margin:0;padding:0}
html,body{width:1200px;height:1000px;overflow:hidden}
body{background:var(--stage);font-family:"Open Sans",Arial,sans-serif;color:var(--ink);position:relative}
.sheet{position:absolute;background:var(--paper);box-shadow:2px 3px 5px rgba(0,0,0,.35);overflow:hidden}
.brand{display:flex;align-items:center;gap:5px;color:var(--blue);font-weight:700;line-height:1.05}
.brand .dot{width:11px;height:11px;border-radius:50%;background:var(--red);flex:none}
.brand .name{font-size:12px;max-width:100px}
.brand.sm .name{font-size:9px;max-width:80px}
.brand.sm .dot{width:8px;height:8px}
.doctors{color:var(--red);font-weight:700;font-size:11.5px;line-height:15px}
.role{font-size:9px;color:var(--ink)}
.addr{color:var(--blue);font-weight:600;font-size:8.5px;line-height:11px}
.phone{display:flex;align-items:center;gap:5px;font-size:9px;line-height:13px}
.phone svg{width:9px;height:8px;fill:var(--red)}
.tagline{color:var(--blue);font-size:9.5px;font-weight:600}
.appt-title{text-align:center;color:var(--blue);font-weight:600;font-size:12.5px}
.appt-row{position:absolute;left:26px;right:26px;font-size:8.5px;display:flex;align-items:flex-end;gap:4px}
.dots{flex:1;border-bottom:1px dotted var(--blue);height:8px}
.days{position:absolute;left:26px;right:26px;display:flex;justify-content:space-between;font-size:8.5px}
.days span{display:flex;align-items:center;gap:4px}
.days i{width:9px;height:9px;border:1px solid var(--blue);display:inline-block}
.notice{position:absolute;left:0;right:0;text-align:center;font-size:8px;color:var(--grey)}
.band{position:absolute;left:0;right:0;background:var(--blue);color:#fff}
.mini-contact{display:flex;gap:6px;font-size:5.5px;color:var(--blue);line-height:9px}
.mini-contact .tel{color:var(--ink)}
.mini-contact .tel b{color:var(--red);font-weight:400}
.mini-contact .loc{border-left:1px solid var(--blue);padding-left:5px}
.stripe{position:absolute;left:0;right:0;bottom:0}
.letter-body{position:absolute;left:36px;width:400px;font-size:8.2px;line-height:16.3px;color:var(--ink)}
.letter-body p{margin-bottom:16px}
.signature{width:120px;height:38px;background:linear-gradient(90deg,#f2f2f2,#e4e4e4);margin:8px 0 8px}
.foot-note{position:absolute;left:34px;bottom:20px;font-size:5.5px;color:var(--blue)}
</style>
</head>
<body>

<section class="sheet card-white" style="left:36px;top:43px;width:294px;height:182px">
  <div style="position:absolute;left:24px;top:18px">
    <div class="doctors">Dr A Halvorsen<br>Dr Z Okafor</div>
    <div class="role">Family Doctors</div>
  </div>
  <div class="brand" style="position:absolute;left:150px;top:22px"><span class="dot"></span><span class="name">Dunmore Glen Medical Clinic</span></div>
  <div class="addr" style="position:absolute;left:24px;top:78px">20418 57 ST NW<br>Edmonton AB<br>T6K 3R8</div>
  <div style="position:absolute;left:24px;top:114px">
    <div class="phone"><svg viewBox="0 0 10 9"><path d="M0 3 Q5 -1 10 3 L8 4 L7 3 L3 3 L2 4Z M2 5 H8 V9 H2Z"/></svg>(780) 555-0142</div>
    <div class="phone"><svg viewBox="0 0 10 9"><rect x="0" y="3" width="10" height="6"/><rect x="2" y="0" width="6" height="3"/></svg>(780) 555-0187</div>
  </div>
  <div class="tagline" style="position:absolute;left:24px;top:150px">Family Practice &amp; walk in Welcome</div>
</section>

<section class="sheet appt-white" style="left:362px;top:43px;width:300px;height:182px">
  <div class="appt-title" style="position:absolute;left:0;right:0;top:10px">Appointment</div>
  <div class="appt-row" style="top:46px"><span>For</span><span class="dots"></span></div>
  <div class="days" style="top:70px"><span><i></i>Sun</span><span><i></i>Mon</span><span><i></i>Tue</span><span><i></i>Wed</span><span><i></i>Thu</span><span><i></i>Fri</span><span><i></i>Sat</span></div>
  <div class="appt-row" style="top:94px"><span>Date</span><span class="dots"></span><span>at</span><span class="dots"></span><span>AM&nbsp;&nbsp;PM</span></div>
  <div class="brand" style="position:absolute;left:96px;top:124px"><span class="dot"></span><span class="name">Dunmore Glen Medical Clinic</span></div>
  <div class="notice" style="top:162px">If unable to keep appointment, kindly notice us before 24 hrs.</div>
</section>

<section class="sheet card-band" style="left:36px;top:262px;width:300px;height:182px">
  <div style="position:absolute;left:24px;top:18px">
    <div class="doctors">Dr A Halvorsen<br>Dr Z Okafor</div>
    <div class="role">Family Doctors</div>
  </div>
  <div class="brand" style="position:absolute;left:26px;top:104px"><span class="dot"></span><span class="name">Dunmore Glen Medical Clinic</span></div>
  <div class="addr" style="position:absolute;left:209px;top:72px">20418 57 ST NW<br>Edmonton AB<br>T6K 3R8</div>
  <div style="position:absolute;left:209px;top:108px">
    <div class="phone"><svg viewBox="0 0 10 9"><path d="M0 3 Q5 -1 10 3 L8 4 L7 3 L3 3 L2 4Z M2 5 H8 V9 H2Z"/></svg>(780) 555-0142</div>
    <div class="phone"><svg viewBox="0 0 10 9"><rect x="0" y="3" width="10" height="6"/><rect x="2" y="0" width="6" height="3"/></svg>(780) 555-0187</div>
  </div>
  <div class="band" style="bottom:0;height:34px;line-height:34px;text-align:center;font-size:10px;font-weight:600">Family Practice &amp; walk in Welcome</div>
</section>

<section class="sheet appt-band" style="left:362px;top:262px;width:300px;height:182px">
  <div class="band" style="top:0;height:30px;line-height:30px;text-align:center;font-size:12.5px;font-weight:600">Appointment</div>
  <div class="appt-row" style="top:48px"><span>For</span><span class="dots"></span></div>
  <div class="days" style="top:73px"><span><i></i>Sun</span><span><i></i>Mon</span><span><i></i>Tue</span><span><i></i>Wed</span><span><i></i>Thu</span><span><i></i>Fri</span><span><i></i>Sat</span></div>
  <div class="appt-row" style="top:98px"><span>Date</span><span class="dots"></span><span>at</span><span class="dots"></span><span>AM&nbsp;&nbsp;PM</span></div>
  <div class="brand" style="position:absolute;left:96px;top:126px"><span class="dot"></span><span class="name">Dunmore Glen Medical Clinic</span></div>
  <div class="notice" style="top:161px">If unable to keep appointment, kindly notice us before 24 hrs.</div>
</section>

<section class="sheet envelope-stripe" style="left:36px;top:476px;width:548px;height:230px">
  <div class="brand sm" style="position:absolute;left:22px;top:22px"><span class="dot"></span><span class="name">Dunmore Glen Medical Clinic</span></div>
  <div class="mini-contact" style="position:absolute;left:22px;top:56px">
    <div class="tel"><b>☎</b> (780) 555-0142<br><b>■</b> (780) 555-0187</div>
    <div class="loc">20418 57 ST NW<br>Edmonton AB, T6K 3R8</div>
  </div>
  <svg class="stripe" width="548" height="20" viewBox="0 0 548 20">
    <polygon points="0,2 394,2 400,20 0,20" fill="var(--blue)"/>
    <polygon points="404,2 548,2 548,20 410,20" fill="var(--red)"/>
  </svg>
</section>

<section class="sheet letterhead" style="left:697px;top:43px;width:463px;height:655px">
  <div class="brand" style="position:absolute;left:36px;top:30px"><span class="dot"></span><span class="name" style="font-size:14px;max-width:125px">Dunmore Glen Medical Clinic</span></div>
  <div class="mini-contact" style="position:absolute;left:352px;top:22px;flex-direction:column;gap:2px;border-left:1px solid var(--blue);padding-left:6px">
    <div class="tel"><b>☎</b> (780) 555-0142<br><b>■</b> (780) 555-0187</div>
    <div>20418 57 ST NW<br>Edmonton AB, T6K 3R8</div>
  </div>
  <div style="position:absolute;left:36px;top:98px;font-size:8.2px;line-height:16.5px;font-weight:600">To<br>Mr. Owen Pritchard<br>Lorem Ipsum is simply a dummy text</div>
  <div class="letter-body" style="top:163px">
    <p>&nbsp;dummy text of the printing and typesetting industry. Lorem Ipsum has been the industry's standard dummy text ever since the 1500s, when an unknown printer took a galley of type and scrambled it to make a type specimen book. It has survived not only five centuries, but also the leap into electronic typesetting, remaining essentially unchanged. It was popularised in the 1960s with the release of Lettrafine sheets containing Lorem Ipsum passages, and more recently with desktop publishing software like Pagewright Studio including versions of Lorem Ipsum.</p>
    <p>It is a long established fact that a reader will be distracted by the readable content of a page when looking at its layout. Many desktop publishing packages and web page editors now use Lorem Ipsum as their default model text, and a search for 'lorem ipsum' will uncover many web sites still in their infancy. Various versions have evolved over the years, sometimes by accident, sometimes on purpose (injected humour and the like).</p>
    <p>&nbsp;Contrary to popular belief, Lorem Ipsum is not simply random text. It has roots in a piece of classical Latin literature from 45 BC, making it over 2000 years old. Edwin Marlow, a Latin professor at Ashgrove College in Vermont, looked up one of the more obscure Latin words, consectetur, from a Lorem Ipsum passage, and going through the cites of the word in classical literature, discovered the undoubtable source. Lorem Ipsum comes from sections 1.10.32 and 1.10.33 of "de Finibus Bonorum et Malorum" (The Extremes of Good and Evil) by Varenius, written in 45 BC. This book</p>
    <div>Lorem Ipsum</div>
    <div class="signature" role="img" aria-label="Handwritten signature"></div>
    <div>Lorem Ipsum is a dummy</div>
  </div>
  <div class="foot-note">Family Doctors &nbsp;|&nbsp; Family Practice &amp; walk in Welcome</div>
  <svg class="stripe" width="463" height="17" viewBox="0 0 463 17">
    <polygon points="0,0 334,0 340,17 0,17" fill="var(--blue)"/>
    <polygon points="344,0 463,0 463,17 350,17" fill="var(--red)"/>
  </svg>
</section>

<section class="sheet envelope-plain" style="left:36px;top:737px;width:548px;height:230px">
  <div class="brand sm" style="position:absolute;left:22px;top:22px"><span class="dot"></span><span class="name">Dunmore Glen Medical Clinic</span></div>
  <div class="mini-contact" style="position:absolute;left:22px;top:56px">
    <div class="tel"><b>☎</b> (780) 555-0142<br><b>■</b> (780) 555-0187</div>
    <div class="loc">20418 57 ST NW<br>Edmonton AB, T6K 3R8</div>
  </div>
</section>

<section class="sheet envelope-back" style="left:612px;top:737px;width:548px;height:230px">
  <svg width="548" height="230" viewBox="0 0 548 230" style="position:absolute;left:0;top:0">
    <path d="M2 0 Q20 70 180 58 L370 58 Q528 70 546 0" fill="none" stroke="var(--line)" stroke-width="1"/>
  </svg>
  <div class="brand sm" style="position:absolute;left:232px;top:16px"><span class="dot"></span><span class="name">Dunmore Glen Medical Clinic</span></div>
</section>

</body>
</html>
```